Business Card for a recruitment agency specializing in engineers and geeks.

I am looking to create Business Card Design for my company.
That
## Company name:
Quorvant Inc.
Quorvant is a term coined from the following concepts.
1. geek + engineer
2. geek utopia
## Company Description:
The concept of the company is to be a recruitment agency that creates a paradise for geeky engineers. We want to be a place where engineers can have more freedom and ideal career support.
# Target.
The noun itself is often given to companies that want to hire engineers, geeks, and IT-related personnel, so it would be nice to get the impression that this company seems to have good engineers and IT personnel. There are many occasions where I meet with the human resources department, president, or senior management and give it to them.
# Atmosphere
We are happy with simplicity, but with an impact that will help people remember the company. The logo is based on a dinosaur that does programming, so it should be somewhat playful, but since it will basically be used in a business setting, please don't make it too silly.
# About the logo
See the attached files. The company logo represents our engineers smiling upward because of our work, with the motif of a dinosaur doing programming.
## Color
We will leave the color scheme to you, but since the logo is in black and white, colors with such a taste would fit well.
## file format
ai, psd, png, svg
Industry/Entity Type
human resource and employment agency
Contact Information for Business Card
Company name, address, email, tel, URL,logo
Colors
Designer to choose colors to be used in the design.

```html
<!DOCTYPE html>
<html lang="en">
<head>
<meta charset="utf-8">
<title>Quorvant Inc. — Business Card</title>
<link href="https://fonts.googleapis.com/css2?family=Arimo:wght@400;700&display=swap" rel="stylesheet">
<style>
  :root {
    --bg: #e9e9ea;
    --card: #2e2d2e;
    --band: #f4f4f4;
    --ink-light: #f2f2f2;
    --ink-soft: #cfcfcf;
    --ink-dark: #2a2a2a;
    --ink-mid: #555555;
  }
  html, body {
    margin: 0;
    padding: 0;
    width: 1200px;
    height: 802px;
    overflow: hidden;
    background: var(--bg);
    font-family: "Arimo", Arial, sans-serif;
  }
  .stage {
    position: relative;
    width: 1200px;
    height: 802px;
  }
  .card {
    position: absolute;
    top: 246px;
    width: 540px;
    height: 309px;
    background: var(--card);
    border-radius: 3px;
    box-shadow: 0 10px 24px rgba(0,0,0,0.18);
    overflow: hidden;
  }
  .card--front { left: 40px; }
  .card--back { left: 620px; }

  /* front */
  .name-band {
    position: absolute;
    left: 0;
    top: 44px;
  }
  .holder {
    position: absolute;
    left: 26px;
    top: 55px;
    color: var(--ink-dark);
  }
  .holder__name {
    font-weight: 700;
    font-size: 19px;
    letter-spacing: 0.2px;
  }
  .holder__role {
    font-size: 12px;
    color: var(--ink-mid);
    margin-top: 3px;
  }
  .brand {
    position: absolute;
    left: 300px;
    top: 53px;
    display: flex;
    align-items: center;
    gap: 10px;
  }
  .brand__dot {
    width: 30px;
    height: 30px;
    background: var(--ink-light);
  }
  .brand__name {
    color: var(--ink-light);
    font-size: 28px;
    font-weight: 400;
    letter-spacing: 0.5px;
  }
  .address {
    position: absolute;
    right: 28px;
    top: 150px;
    text-align: right;
    color: var(--ink-soft);
    font-size: 13px;
    line-height: 1.35;
  }
  .contacts {
    position: absolute;
    left: 26px;
    bottom: 26px;
    margin: 0;
    padding: 0;
    list-style: none;
    color: var(--ink-soft);
    font-size: 13px;
    line-height: 1.5;
  }
  .contacts li {
    display: flex;
    align-items: center;
    gap: 8px;
  }
  .contacts svg { width: 11px; height: 11px; fill: none; stroke: var(--ink-soft); stroke-width: 1.4; }

  /* back */
  .back-brand {
    position: absolute;
    inset: 0;
    display: flex;
    align-items: center;
    justify-content: center;
    color: var(--ink-light);
    font-size: 62px;
    font-weight: 400;
    letter-spacing: 1px;
  }
</style>
</head>
<body>
<main class="stage">
  <section class="card card--front" aria-label="Business card front">
    <svg class="name-band" width="300" height="70" viewBox="0 0 300 70" aria-hidden="true">
      <polygon points="0,0 272,0 292,35 272,70 0,70" fill="var(--band)"/>
    </svg>
    <div class="holder">
      <div class="holder__name">Daniel Reyes</div>
      <div class="holder__role">Manager</div>
    </div>
    <div class="brand">
      <span class="brand__dot" aria-hidden="true"></span>
      <span class="brand__name">Quorvant</span>
    </div>
    <div class="address">Your address, city<br>state, ZIP 0000</div>
    <ul class="contacts">
      <li>
        <svg viewBox="0 0 12 12" aria-hidden="true"><path d="M3 1 L5 3.5 L4 5 Q5.5 7.5 7 8 L8.5 7 L11 9 L9.5 11 Q4 10.5 1 3 Z"/></svg>
        123-456-2100
      </li>
      <li>
        <svg viewBox="0 0 12 12" aria-hidden="true"><rect x="1" y="2.5" width="10" height="7"/><path d="M1 2.5 L6 6.5 L11 2.5"/></svg>
        youremail@mailbox.com
      </li>
      <li>
        <svg viewBox="0 0 12 12" aria-hidden="true"><circle cx="6" cy="6" r="5"/><path d="M1 6 H11 M6 1 Q3 6 6 11 M6 1 Q9 6 6 11"/></svg>
        www.yourwebsite.com
      </li>
    </ul>
  </section>

  <section class="card card--back" aria-label="Business card back">
    <div class="back-brand">Quorvant</div>
  </section>
</main>
</body>
</html>
```